Financial Services Company

We need a wordpress design for an existing company based in Boston called Tolvey Capital. We help private investment firms with their fundraising activities. Our website will be pretty static, with occasional news item updates. We have an existing site at www.tolveycapital-example.com. Our new site will have one additional page and a few text updates. Please use our existing color schema of greens and whites. Our logo is in Constantina font. The color of the font is 0,100,55.

Similar sites:
brindlecapitaladvisors-example.com
http://www.morvanpartnersllc-example.com/
www.quillmont-example.com
www.lumberwick-example.com
rtvgo-example.com

Industry/Entity Type

Investment

Requirements
Must have
• We want to have the page tabs at the top of the site. The front page should include a newsfeed that we can update in wordpress with new information.

```html
<!DOCTYPE html>
<html lang="en">
<head>
<meta charset="utf-8">
<title>Tolvey Capital</title>
<link href="https://fonts.googleapis.com/css2?family=Sorts+Mill+Goudy&family=Open+Sans:wght@700&display=swap" rel="stylesheet">
<style>
  :root{
    --green:#00643a;
    --green-soft:#2f6a52;
    --rule:#3f6e5c;
    --tab-active:#a5b493;
    --text:#2c2c2c;
    --nav-text:#1f1f1f;
    --footer:#c8c8cc;
    --hero-a:#e9e9e9;
    --hero-b:#8a8a8a;
    --wash:#e6f1d3;
  }
  *{margin:0;padding:0;box-sizing:border-box}
  html,body{width:1200px;height:993px;overflow:hidden}
  body{
    position:relative;
    font-family:"Sorts Mill Goudy",Georgia,serif;
    color:var(--text);
    background:
      radial-gradient(ellipse 380px 300px at 0 0,var(--wash),transparent 70%),
      radial-gradient(ellipse 420px 340px at 1200px 0,var(--wash),transparent 70%),
      radial-gradient(ellipse 300px 420px at 0 500px,#eef5e2,transparent 70%),
      radial-gradient(ellipse 300px 420px at 1200px 500px,#eef5e2,transparent 70%),
      #fdfefb;
  }
  .brand{position:absolute;left:157px;top:88px;display:flex;align-items:center;gap:10px;
    color:var(--green);font-size:26px;line-height:1}
  .brand-mark{width:14px;height:14px;background:var(--green)}

  .nav{position:absolute;left:147px;top:136px;width:891px;height:45px;
    background:linear-gradient(#f4f4f4,#fdfdfd 40%,#e9e9e9);border:1px solid #d6d6d6;
    font-size:17px;color:var(--nav-text)}
  .nav a,.nav .sep{position:absolute;top:0;height:100%;display:flex;align-items:center;justify-content:center;color:inherit;text-decoration:none}
  .nav .active{background:var(--tab-active)}
  .nav .sep{font-size:13px;color:#555}

  .hero{position:absolute;left:147px;top:181px;width:891px;height:383px;
    background:linear-gradient(100deg,var(--hero-a),#c9c9c9 35%,#b0b0b0 55%,#d8d8d8 80%,var(--hero-b))}

  .col{position:absolute;top:574px}
  .col-head{display:flex;align-items:center;gap:10px;height:36px;border-bottom:1.5px solid var(--rule);
    font-family:"Open Sans",sans-serif;font-weight:700;font-size:22px;color:var(--green-soft)}
  .about{left:147px;width:305px}
  .news{left:493px;width:277px}
  .contact{left:825px;width:208px}
  .about .col-head{padding-left:6px}
  .news .col-head{padding-left:18px}
  .contact .col-head{padding-left:16px}

  .about p{font-size:13px;line-height:13.3px;letter-spacing:.4px;margin:0 0 12px 10px;width:300px}
  .about .body{margin-top:29px}

  .news ul{list-style:none;margin-top:22px;margin-left:-6px}
  .news li{font-size:12.5px;line-height:14px;padding-left:9px;position:relative;margin-bottom:14px;width:300px}
  .news li::before{content:"";position:absolute;left:0;top:6px;width:3px;height:3px;border-radius:50%;background:var(--green)}

  .dots{position:absolute;left:796px;top:642px;height:245px;border-left:1px dotted #777}

  .contact .block{font-size:12.5px;line-height:14px;padding:10px 0 8px 0;border-bottom:1.5px dotted #555;width:208px;margin-top:4px}
  .contact .block:last-of-type{border-bottom:none}
  .contact .first{margin-top:18px}

  .more{position:absolute;top:889px;font-size:12.5px;color:var(--text)}
  .more::before{content:"›";margin-right:4px}

  .footer{position:absolute;left:150px;top:910px;width:890px;height:83px;background:var(--footer);font-size:11.5px;color:#333}
  .footer .copy{position:absolute;left:22px;top:16px;display:flex;align-items:center;gap:4px}
  .footer .links{position:absolute;right:72px;top:12px;word-spacing:2px}
  .footer .links span{color:#666;padding:0 6px}
  .footer .legal{position:absolute;right:62px;top:54px}
  .footer .legal b{font-weight:400;margin-left:22px}
</style>
</head>
<body>

<div class="brand">
  <span class="brand-mark"></span>
  <span class="brand-name">Tolvey Capital</span>
</div>

<nav class="nav">
  <a class="active" href="#" style="left:198px;width:85px">Home</a>
  <a href="#" style="left:284px;width:80px">Team</a>
  <span class="sep" style="left:366px;width:10px">|</span>
  <a href="#" style="left:390px;width:96px">Assignments</a>
  <span class="sep" style="left:499px;width:10px">|</span>
  <a href="#" style="left:522px;width:90px">Secondaries</a>
  <span class="sep" style="left:621px;width:10px">|</span>
  <a href="#" style="left:645px;width:50px">News</a>
  <span class="sep" style="left:716px;width:10px">|</span>
  <a href="#" style="left:740px;width:84px">Contact Us</a>
</nav>

<div class="hero" role="img" aria-label="Black and white photograph of three colleagues reviewing documents together in an office"></div>

<section class="col about">
  <h2 class="col-head">
    <svg width="36" height="28" viewBox="0 0 36 28"><circle cx="18" cy="8" r="7" fill="#6f9a88"/><path d="M2 28c1-9 8-12 16-12s15 3 16 12z" fill="#6f9a88"/></svg>
    About Us
  </h2>
  <div class="body">
    <p>Tolvey Capital Advisers (“Tolvey”) provides fund placement and advisory services to private equity and venture capital firms. Tolvey was co-founded by Alden Pryce and Rupert Calloway and is an institutional division of Meridale Securities Corporation, Member NRSA SIPF.</p>
    <p>We have over 25 years experience building private equity firms from the inside, and our founders have each had a key role building a top-performing investment firm.</p>
    <p>We have raised $1.5 billion in commitments from leading investors around the globe. Our heritage as former private equity investment professionals provides us with an investor-focused perspective to fundraising that sets us apart from traditional placement firms.</p>
  </div>
</section>

<section class="col news">
  <h2 class="col-head">
    <svg width="30" height="28" viewBox="0 0 30 28"><circle cx="10" cy="7" r="5" fill="#6f9a88"/><circle cx="20" cy="7" r="5" fill="#4f7d6b"/><rect x="3" y="14" width="12" height="14" rx="2" fill="#6f9a88"/><rect x="14" y="14" width="12" height="14" rx="2" fill="#4f7d6b"/></svg>
    News
  </h2>
  <ul>
    <li>Tolvey Capital hires Martin Vesper as Vice President</li>
    <li>Ashcombe II closes on $224 million</li>
    <li>Rupert Calloway speaks at National Forum for Middle Market Funds</li>
    <li>Alden Pryce speaks at NEBTA Cross-Border Technology Business Forum</li>
    <li>Kestrel III closes at $244 million</li>
    <li>Alden Pryce judges VCQX competition</li>
    <li>Brookhollow named Best New Buyout Firm of 2008</li>
    <li>How Some Firms Beat Fundraising Odds</li>
  </ul>
</section>

<div class="dots"></div>

<section class="col contact">
  <h2 class="col-head">
    <svg width="22" height="28" viewBox="0 0 22 28"><path d="M5 2l5 1 1 7-4 2c1 5 3 8 6 10l3-3 5 3-1 5c-3 2-9 0-13-6S1 7 5 2z" fill="#6f9a88"/></svg>
    Contact Us
  </h2>
  <div class="block first">Tolvey Capital Advisers<br>48 Linden Wharf, Suite 700<br>Boston, MA 02199<br>Main (617) 555-0142</div>
  <div class="block">Alden Pryce<br>Managing Director<br>Alden@TolveyCapital-example.com<br>Direct: (617) 555-0187</div>
  <div class="block">Rupert Calloway<br>Managing Director<br>Rupert@TolveyCapital-example.com<br>Direct: (240) 555-0163</div>
</section>

<a class="more" style="left:159px">More</a>
<a class="more" style="left:494px">More</a>
<a class="more" style="left:827px">More</a>

<footer class="footer">
  <div class="copy">
    <svg width="15" height="15" viewBox="0 0 15 15"><circle cx="7.5" cy="7.5" r="6.5" fill="none" stroke="#222" stroke-width="1.3"/><path d="M10 5.2a3 3 0 1 0 0 4.6" fill="none" stroke="#222" stroke-width="1.3"/></svg>
    2012 Tolvey Capital Advisers
  </div>
  <div class="links">Home<span>|</span>Team<span>|</span>Assigments<span>|</span>Secondaries<span>|</span>News<span>|</span>Contact Us</div>
  <div class="legal">Securities offered through Meridale Securities Corporation <b>Member NRSA SIPF</b></div>
</footer>

</body>
</html>
```